Visitenkarten für eine Hypnose-Praxis
Ich bin sehr zufrieden mit der professionellen Arbeitsweise von KOR7342. Es war immer ein netter Kontakt und meine Wünsche wurden schnell umgesetzt. Alle Vorschläge waren sehr kreativ und und so viel es mir leicht, eine schnelle Entscheidung zu treffen.
Zielgruppe
Wir sind eine Hypnose-Praxis und richten unser Angebot an Privatpersonen unterschiedlichen Alters, die therapeutische Unterstützung suchen.
Aufgabenstellung
Eher schlichtes und modernes Design

```html
<!DOCTYPE html>
<html lang="de">
<head>
<meta charset="utf-8">
<title>sanftwelle – Visitenkarte</title>
<link href="https://fonts.googleapis.com/css2?family=Open+Sans:wght@400;600&display=swap" rel="stylesheet">
<style>
  :root {
    --bg: #e4e4e4;
    --card: #fbfbfb;
    --ink: #2b2b2b;
    --ink-soft: #555555;
    --rule: #9a9a9a;
    --accent: #5aaec9;
    --shadow: rgba(0, 0, 0, 0.12);
  }
  html, body {
    margin: 0;
    padding: 0;
    width: 1200px;
    height: 525px;
    overflow: hidden;
    background: var(--bg);
    font-family: "Open Sans", Arial, sans-serif;
    color: var(--ink);
  }
  .stage {
    position: relative;
    width: 1200px;
    height: 525px;
  }
  .card {
    position: absolute;
    top: 112px;
    height: 300px;
    background: var(--card);
    border-radius: 10px;
    box-shadow: 0 6px 18px var(--shadow), 0 1px 3px var(--shadow);
    box-sizing: border-box;
  }
  /* Front side */
  .card-front {
    left: 50px;
    width: 540px;
    display: flex;
    align-items: center;
    padding: 0 40px 0 56px;
  }
  .brand {
    display: flex;
    align-items: center;
    gap: 14px;
  }
  .brand-square {
    width: 30px;
    height: 30px;
    border-radius: 3px;
    background: var(--accent);
  }
  .brand-name {
    font-size: 34px;
    font-weight: 600;
    color: var(--ink);
    letter-spacing: -0.5px;
  }
  .divider {
    width: 1px;
    height: 100px;
    background: var(--rule);
    margin: 0 24px 0 26px;
  }
  .contact-name {
    font-size: 20px;
    font-weight: 600;
    margin: 0;
  }
  .contact-title {
    font-size: 13px;
    color: var(--ink-soft);
    margin: 2px 0 18px;
  }
  .contact-line {
    font-size: 12.5px;
    color: var(--ink);
    margin: 2px 0;
  }
  /* Back side */
  .card-back {
    left: 660px;
    width: 490px;
    display: flex;
    flex-direction: column;
    align-items: center;
    padding-top: 56px;
    text-align: center;
  }
  .back-square {
    width: 34px;
    height: 34px;
    border-radius: 3px;
    background: var(--accent);
  }
  .back-claim {
    margin: 48px 0 0;
    width: 330px;
    font-size: 12.5px;
    line-height: 1.45;
    color: var(--ink);
  }
  .back-web {
    margin-top: 34px;
    font-size: 12.5px;
    color: var(--ink);
  }
</style>
</head>
<body>
<main class="stage">
  <section class="card card-front" aria-label="Vorderseite">
    <div class="brand">
      <span class="brand-square" aria-hidden="true"></span>
      <span class="brand-name">sanftwelle</span>
    </div>
    <div class="divider" aria-hidden="true"></div>
    <div class="contact">
      <p class="contact-name">Lena Hofmann</p>
      <p class="contact-title">Dipl.-Psychologin</p>
      <p class="contact-line">Telefon: +49 555 0192837</p>
      <p class="contact-line">Website: www.sanftwelle-praxis.de</p>
    </div>
  </section>

  <section class="card card-back" aria-label="Rückseite">
    <span class="back-square" aria-hidden="true"></span>
    <p class="back-claim">Wir sind eine Hypnose-Praxis und richten unser Angebot an Privatpersonen unterschiedlichen Alters, die therapeutische Unterstützung suchen.</p>
    <p class="back-web">www.sanftwelle-praxis.de</p>
  </section>
</main>
</body>
</html>
```